T.B.W.L. Business Card Design

we need a business card design for a motor vehicle repair business in Southport Australia, called Trevan's Automotive Repair Services. Our services include panel & paint, resprays and light bodyworks. We have a logo which we would like to use on the business card. We would like to see designs that use the colours blue and grey.

Industry/Entity Type

Automotive

Contact Information for Business Card

Trevan's Automotive Repair Services,
Delwyn Orsk,
7/2-4 Quarrow Street Kellerby 4290, 0471 862 307, /trevansautomotiverepairservices, trevansautomotiverepairservices@examplemail.test,
services: panel & paint, respray, light bodyworks.
ABN: 47 612 098 254

Requirements
Must have
• Front of card must include attached logo and contact details.
please list services
Your eye should be drawn to the name (Delwyn Orsk) and phone number (0471 862 307).
Font must be legible and contemporary.
back of business card should have the following:
1. title - quote and
2. list the following: for, date, valid till, quote details and
3. a footer "to book you repair, please contact Delwyn Orsk on 0471 862 307".
There needs to be enough space to hand write details.
Should not have
• do not include any graphics/illustrations.

```html
<!DOCTYPE html>
<html lang="en">
<head>
<meta charset="utf-8">
<title>Trevan's Automotive Repair Services – Business Card</title>
<link rel="stylesheet" href="https://fonts.googleapis.com/css2?family=Mukta:wght@400;500;700&family=Roboto+Condensed:wght@400&display=swap">
<style>
  :root {
    --page: #ecebe8;
    --card-light: #e6e6e6;
    --card-white: #ffffff;
    --slate: #5a5b5d;
    --brand-blue: #2a7cc0;
    --band-blue: #2f82c4;
    --ink: #1d1d1f;
    --rule: #6c6c6c;
    --on-dark: #ffffff;
  }
  * { box-sizing: border-box; margin: 0; padding: 0; }
  html, body { width: 1200px; height: 1200px; overflow: hidden; }
  body {
    background: var(--page);
    font-family: "Mukta", "Helvetica Neue", Arial, sans-serif;
    color: var(--ink);
    position: relative;
  }
  .card {
    position: absolute;
    left: 150px;
    width: 900px;
    height: 514px;
    overflow: hidden;
    box-shadow: 0 6px 18px rgba(0,0,0,0.18);
  }

  /* Front */
  .card--front { top: 60px; background: var(--card-light); }
  .front__panel { position: absolute; inset: 0; width: 900px; height: 514px; }
  .brand {
    position: absolute; left: 60px; top: 70px;
    display: flex; align-items: center; gap: 18px;
  }
  .brand__dot {
    width: 58px; height: 58px; border-radius: 50%;
    background: var(--brand-blue); flex: none;
  }
  .brand__name {
    color: var(--brand-blue);
    font-weight: 700;
    font-size: 40px;
    line-height: 1.02;
    text-transform: uppercase;
    letter-spacing: 0.5px;
  }
  .contact { position: absolute; left: 60px; top: 282px; }
  .contact__name { font-size: 42px; font-weight: 400; line-height: 1.05; }
  .contact__address { font-size: 22px; line-height: 1.3; margin-top: 2px; }
  .contact__phone { font-size: 40px; font-weight: 500; line-height: 1.15; margin-top: 8px; }
  .contact__email { font-size: 21px; line-height: 1.3; }
  .services {
    position: absolute; right: 50px; top: 120px;
    color: var(--on-dark);
    text-align: right;
  }
  .services__title { font-size: 27px; font-weight: 400; letter-spacing: 0.5px; margin-bottom: 26px; }
  .services__list { list-style: none; font-size: 29px; font-weight: 500; line-height: 1.22; }

  /* Back */
  .card--back {
    top: 626px; background: var(--card-white);
    font-family: "Roboto Condensed", "Arial Narrow", sans-serif;
  }
  .back__title {
    height: 112px; background: var(--band-blue);
    color: var(--on-dark);
    display: flex; align-items: center; justify-content: center;
    font-size: 44px; font-weight: 400; letter-spacing: 0.5px;
  }
  .quote-form { list-style: none; padding: 44px 0 0 140px; }
  .quote-form__row {
    display: flex; align-items: flex-end; height: 56px;
    font-size: 27px;
  }
  .quote-form__label { width: 215px; }
  .quote-form__colon { width: 20px; }
  .quote-form__line { width: 430px; border-bottom: 2px solid var(--rule); height: 30px; }
  .back__footer {
    position: absolute; left: 0; right: 0; bottom: 0; height: 102px;
    background: var(--slate);
    color: var(--on-dark);
    display: flex; align-items: center; justify-content: center;
    font-size: 27px; letter-spacing: 0.3px;
  }
</style>
</head>
<body>
  <section class="card card--front" aria-label="Business card front">
    <svg class="front__panel" viewBox="0 0 900 514" aria-hidden="true">
      <polygon points="690,0 900,0 900,514 600,514" fill="var(--slate)"/>
    </svg>
    <div class="brand">
      <span class="brand__dot" aria-hidden="true"></span>
      <span class="brand__name">Trevan's Automotive<br>Repair Services</span>
    </div>
    <div class="contact">
      <p class="contact__name">Delwyn Orsk</p>
      <p class="contact__address">7/2-4 Quarrow Street Kellerby 4290</p>
      <p class="contact__phone">0471 862 307</p>
      <p class="contact__email">trevansautomotiverepairservices@examplemail.test</p>
    </div>
    <div class="services">
      <p class="services__title">OUR SERVICES</p>
      <ul class="services__list">
        <li>panel &amp; paint</li>
        <li>respray</li>
        <li>light bodyworks</li>
      </ul>
    </div>
  </section>

  <section class="card card--back" aria-label="Business card back, quote form">
    <h1 class="back__title">Trevan's Automotive Repair Services</h1>
    <ul class="quote-form">
      <li class="quote-form__row"><span class="quote-form__label">For</span><span class="quote-form__colon">:</span><span class="quote-form__line"></span></li>
      <li class="quote-form__row"><span class="quote-form__label">Date</span><span class="quote-form__colon">:</span><span class="quote-form__line"></span></li>
      <li class="quote-form__row"><span class="quote-form__label">Valid till</span><span class="quote-form__colon">:</span><span class="quote-form__line"></span></li>
      <li class="quote-form__row"><span class="quote-form__label">Quote details</span><span class="quote-form__colon">:</span><span class="quote-form__line"></span></li>
    </ul>
    <p class="back__footer">to book you repair, please contact Delwyn Orsk on 0471 862 307</p>
  </section>
</body>
</html>
```